Website Design for a "Talent Recruitment Agency"

We are looking for a website design for the website of our "Talent Recruitment Agency"; which is called "Crestway Hub".
Our recruitment website "Crestway Hub" will be focusing on: "Crestway Hub: Linking People & Firms in Switzerland"; which means our target audience is two-folded:
(i) TALENT - that is currently residing in- or outside of Switzerland, and is open for and interested in the "Swiss Job Market".
(ii) COMPANIES - that are looking for talent for specific job vacancies in Switzerland.
With our "Crestway Hub" approach we inted to focus on Membership & Partnership:
(a)"Membership"(TALENT)
and
(b)"Partnership"(COMPANIES)
Some of the competitor sites we like are:
• www.plimora42.dk
• www.qelvo.ch
• www.brandolix.ch/en
A sitemap example of our website is attached.
Also attached is a "Crestway Hub" logo in .eps format and one in .jpeg format.
We very much look forward to receive your creative ideas.
Best regards,
Crestway Hub
Crestway Hub: Linking People & Firms in Switzerland.
Website: crestwayhub.ch - Chirpline: CrestwayHubCH
Target Market(s)
(i) TALENT (with around 0-10 years of working experience), currently residing in- or outside of Switzerland, but eligible to work in Switzerland.
(ii) COMPANIES (national or international) that are based in Switzerland.
Industry/Entity Type
Recruitment

```html
<!DOCTYPE html>
<html lang="en">
<head>
<meta charset="utf-8">
<title>Crestway Hub — Linking People &amp; Firms in Switzerland</title>
<link href="https://fonts.googleapis.com/css2?family=Figtree:wght@300;400;600;700&family=Roboto+Condensed:wght@400;700&display=swap" rel="stylesheet">
<style>
:root{
  --orange:#f4511e;
  --blue:#1d86cf;
  --blue-deep:#1b5ea3;
  --navy:#173f6b;
  --text:#444;
  --muted:#666;
  --topbar:#dde9f3;
  --section-grey:#f2f2f2;
  --footer:#e9e9e9;
  --bottom:#3b3b3b;
  --link:#2a7ec8;
}
*{margin:0;padding:0;box-sizing:border-box}
html,body{width:1024px;height:1200px;overflow:hidden}
body{font-family:"Figtree",sans-serif;color:var(--text);background:#fff;position:relative}
.abs{position:absolute}

/* top bar */
.topbar{left:0;top:0;width:1024px;height:24px;background:var(--topbar)}
.langs{left:669px;top:0;height:24px;width:112px;display:flex;gap:8px;align-items:center;padding-left:5px}
.langs .active{background:#fff}
.account{left:808px;top:6px;font-size:9px;color:#6a7a88;display:flex;gap:24px}

/* header */
.header{left:0;top:24px;width:1024px;height:82px;background:#fff;border-bottom:1px solid #e4e4e4}
.brand{display:flex;align-items:center;gap:10px}
.brand .mark{width:30px;height:30px;border-radius:50%;background:var(--orange)}
.brand .name{font-weight:600;color:var(--orange);letter-spacing:-.3px;white-space:nowrap}
.header .brand{position:absolute;left:134px;top:20px}
.header .brand .name{font-size:31px}
.nav{position:absolute;left:502px;top:35px;display:flex;font-size:12px;color:#444}
.nav span{padding:0 10px;border-left:1px solid #ccc;line-height:11px}
.nav span:first-child{border:0;padding-left:1px;color:var(--orange);font-weight:600}
.nav-underline{position:absolute;left:502px;top:78px;width:36px;height:3px;background:var(--orange)}

/* hero */
.hero{left:0;top:106px;width:1024px;height:399px;background:linear-gradient(180deg,#7fa9cf 0%,#5b93c6 100%)}
.hero-photo{left:100px;top:106px;width:340px;height:399px;background:linear-gradient(180deg,#a9988c,#7b8694)}
.hero-panel{left:471px;top:205px;width:553px;height:193px;background:rgba(29,134,207,.95)}
.hero-title{left:525px;top:228px;font-size:36px;line-height:37px;font-weight:700;color:#fff;letter-spacing:-.5px}
.hero-sub{left:527px;top:322px;font-size:18px;line-height:23px;font-weight:300;color:#fff}
.arrow{top:266px;width:49px;height:48px;background:var(--navy);opacity:.85;display:flex;align-items:center;justify-content:center}
.dots{left:140px;top:480px;display:flex;gap:8px}
.dots i{width:8px;height:8px;border-radius:50%;background:rgba(255,255,255,.45)}
.dots i.on{background:var(--blue);border:2px solid #fff;width:10px;height:10px;margin-top:-1px}

/* audience band */
.band{left:0;top:505px;width:1024px;height:285px;background:linear-gradient(180deg,#1f63a9 0%,#2c7fc4 55%,#4ba2db 100%)}
.band-sheen{left:644px;top:505px;width:380px;height:285px;background:rgba(255,255,255,.06);clip-path:polygon(4% 0,100% 0,100% 100%,0 100%)}
.card{top:544px;width:368px;height:210px;background:linear-gradient(90deg,#f3f6f8,#fdfdfd);border-bottom:3px solid #dfe6ec;overflow:hidden}
.card .photo{position:absolute;top:0;height:207px}
.card p{position:absolute;font-size:19px;line-height:28px;font-weight:300;color:#333}
.btn{position:absolute;width:136px;height:42px;background:var(--orange);color:#fff;font-weight:700;font-size:14px;display:flex;align-items:center;justify-content:center;border-radius:2px;border-bottom:2px solid #c73d12}

/* listings */
.listings{left:0;top:790px;width:1024px;height:202px;background:var(--section-grey)}
.sec-title{font-weight:700;font-size:14px;letter-spacing:.5px;color:#444;text-transform:uppercase}
.rule{height:6px;background:repeating-linear-gradient(135deg,#d6d6d6 0 1px,transparent 1px 3px)}
.job-card{left:138px;top:850px;width:496px;height:115px;background:#fff;border:1px solid #e6e6e6}
.job-photo{left:158px;top:869px;width:73px;height:73px;background:linear-gradient(180deg,#8aa8c4,#3b4a5e);border:2px solid #fff;box-shadow:0 0 0 1px #ddd}
.job-icon{top:931px;width:17px;height:15px;background:var(--blue)}
.job-title{left:250px;top:870px;font-family:"Roboto Condensed",sans-serif;font-weight:700;font-size:13px;color:#333}
.job-loc{left:250px;top:885px;font-family:"Roboto Condensed",sans-serif;font-size:10.5px;color:#777}
.job-text{left:250px;top:916px;width:370px;font-size:10.5px;line-height:15px;color:#555}
.job-text a{color:var(--link);text-decoration:none}
.pager{left:495px;top:876px;display:flex;gap:5px}
.pager i{width:7px;height:7px;border-radius:50%;background:#e2e2e2}
.pager i.on{background:var(--blue)}
.event-photo{left:646px;width:44px;height:43px;background:linear-gradient(135deg,#7d8ea0,#2f3a48)}
.event-text{left:701px;width:190px;font-size:10px;line-height:16px;color:#3567a1}
.event-date{left:701px;font-size:8px;font-style:italic;color:#777}

/* footer */
.footer{left:0;top:992px;width:1024px;height:170px;background:var(--footer)}
footer .brand{position:absolute;left:138px;top:1022px}
footer .brand .name{font-size:24px}
footer .brand .mark{width:26px;height:26px}
.about{left:136px;top:1066px;width:220px;font-size:10.5px;line-height:16px;color:#444}
.col-head{font-family:"Roboto Condensed",sans-serif;font-weight:400;font-size:13px;color:#333;top:1018px}
.links{top:1043px;list-style:none;font-size:11px;color:#666}
.links li{height:24px}
.links li::before{content:"›";color:var(--blue);margin-right:8px}
.bottom{left:0;top:1162px;width:1024px;height:38px;background:var(--bottom);color:#8e8e8e;font-size:11px;padding:13px 0 0 136px}
.bottom b{color:#eee;font-weight:400}
</style>
</head>
<body>

<div class="abs topbar"></div>
<div class="abs langs">
  <svg width="22" height="24" class="active" viewBox="0 0 22 24"><rect x="2" y="7" width="18" height="11" fill="#24398a"/><path d="M2 7l18 11M20 7L2 18" stroke="#fff" stroke-width="2"/><path d="M11 7v11M2 12.5h18" stroke="#fff" stroke-width="3.5"/><path d="M11 7v11M2 12.5h18" stroke="#d22" stroke-width="1.8"/></svg>
  <svg width="20" height="12"><rect width="7" height="12" fill="#2a9a3e"/><rect x="7" width="6" height="12" fill="#fff"/><rect x="13" width="7" height="12" fill="#d22"/></svg>
  <svg width="20" height="12"><rect width="20" height="4" fill="#222"/><rect y="4" width="20" height="4" fill="#d22"/><rect y="8" width="20" height="4" fill="#f3c200"/></svg>
  <svg width="20" height="12"><rect width="7" height="12" fill="#2a4fa3"/><rect x="7" width="6" height="12" fill="#fff"/><rect x="13" width="7" height="12" fill="#d22"/></svg>
</div>
<div class="abs account"><span>Login</span><span>Register</span></div>

<header class="abs header">
  <div class="brand"><span class="mark"></span><span class="name">Crestway Hub</span></div>
  <nav class="nav"><span>Home</span><span>About</span><span>Talent</span><span>Companies</span><span>Jobs</span><span>Events</span><span>Contact</span></nav>
  <div class="nav-underline"></div>
</header>

<section>
  <div class="abs hero" role="img" aria-label="Blurred glass office towers in blue tones"></div>
  <div class="abs hero-photo" role="img" aria-label="Smiling businesswoman in a grey blazer"></div>
  <div class="abs hero-panel"></div>
  <h1 class="abs hero-title">We always bring<br>excellence.</h1>
  <p class="abs hero-sub">Linking People &amp; Firms<br>in Switzerland.</p>
  <div class="abs arrow" style="left:0"><svg width="12" height="16"><path d="M9 2L3 8l6 6" stroke="#fff" stroke-width="2" fill="none"/></svg></div>
  <div class="abs arrow" style="left:977px"><svg width="12" height="16"><path d="M3 2l6 6-6 6" stroke="#fff" stroke-width="2" fill="none"/></svg></div>
  <div class="abs dots"><i></i><i class="on"></i><i></i><i></i></div>
</section>

<section>
  <div class="abs band"></div>
  <div class="abs band-sheen"></div>
  <div class="abs card" style="left:136px">
    <div class="photo" role="img" aria-label="Smiling young woman in a dark jacket" style="left:0;width:180px;background:linear-gradient(90deg,#4a3a34,#c9a894 50%,#eef1f3)"></div>
    <p style="right:32px;top:36px;text-align:right">Interested in the<br>Swiss Job Market?</p>
    <a class="btn" style="left:200px;top:134px">Register Now</a>
  </div>
  <div class="abs card" style="left:520px">
    <div class="photo" role="img" aria-label="Businessman in a suit working at a laptop" style="right:0;width:170px;background:linear-gradient(90deg,#eef1f3,#c9a894 45%,#1d2a44)"></div>
    <p style="left:32px;top:34px">Looking for talent for<br>specific job vacancies<br>in Switzerland?</p>
    <a class="btn" style="left:32px;top:134px">Post a Job</a>
  </div>
</section>

<section>
  <div class="abs listings"></div>
  <div class="abs rule" style="left:138px;top:824px;width:184px"></div>
  <h2 class="abs sec-title" style="left:342px;top:815px">Latest Jobs</h2>
  <div class="abs rule" style="left:454px;top:824px;width:180px"></div>
  <div class="abs rule" style="left:646px;top:825px;width:52px"></div>
  <h2 class="abs sec-title" style="left:706px;top:817px">Recent Events</h2>
  <div class="abs rule" style="left:834px;top:825px;width:54px"></div>

  <div class="abs job-card"></div>
  <div class="abs job-photo" role="img" aria-label="Portrait of a job candidate in a suit"></div>
  <div class="abs job-icon" style="left:176px"><svg width="17" height="15"><circle cx="8" cy="7" r="3" stroke="#fff" stroke-width="1.3" fill="none"/><path d="M10 9l3 3" stroke="#fff" stroke-width="1.3"/></svg></div>
  <div class="abs job-icon" style="left:196px"><svg width="17" height="15"><path d="M6 10l5-5" stroke="#fff" stroke-width="1.3"/><rect x="9" y="3" width="4" height="4" rx="1.5" stroke="#fff" fill="none"/><rect x="4" y="8" width="4" height="4" rx="1.5" stroke="#fff" fill="none"/></svg></div>
  <div class="abs job-title">Front-End Developer at &nbsp;Codeloft</div>
  <div class="abs job-loc">Sydney, Australia</div>
  <p class="abs job-text">Lorem ipsum dolor sit amet, consectetur adipisicing elit. Proin nibh augue, suscipit a, scelerisque sed, lacinia in, mi. <a>Read More</a></p>
  <div class="abs pager"><i class="on"></i><i></i><i></i><i></i><i></i><i></i><i></i><i></i><i></i><i></i></div>

  <div class="abs event-photo" style="top:851px" role="img" aria-label="Business people at a networking event"></div>
  <p class="abs event-text" style="top:847px">Fusce gravida tortor felis, ac dictum risus lorem ipsum dolor isment sagittis.</p>
  <p class="abs event-date" style="top:882px">October 15, 2013</p>
  <div class="abs event-photo" style="top:914px" role="img" aria-label="Hands holding a tablet with charts"></div>
  <p class="abs event-text" style="top:910px">Fusce gravida tortor felis, ac dictum risus lorem ipsum dolor isment sagittis.</p>
  <p class="abs event-date" style="top:944px">October 15, 2013</p>
</section>

<footer>
  <div class="abs footer"></div>
  <div class="brand"><span class="mark"></span><span class="name">Crestway Hub</span></div>
  <p class="abs about">Lorem ipsum dolor sit amet, consectetur adipisicing elit. Proin nibh augue, suscipit a, scelerisque sed, lacinia in, mi. Praesent sodales velit quis augue. Cras suscipit.</p>
  <h3 class="abs col-head" style="left:391px">NAVIGATION</h3>
  <ul class="abs links" style="left:392px"><li>Home</li><li>Jobs</li><li>Candidates</li><li>Partners</li></ul>
  <ul class="abs links" style="left:496px"><li>About Us</li><li>Contact Us</li><li>Terms &amp; Conditions</li><li>Privacy Policy</li></ul>
  <h3 class="abs col-head" style="left:647px">FOLLOW US</h3>
  <ul class="abs links" style="left:648px"><li>Blog</li><li>Chirpline</li><li>Friendwall</li><li>Linkwork</li></ul>
  <h3 class="abs col-head" style="left:775px">POPULAR JOBS</h3>
  <ul class="abs links" style="left:776px"><li>Web Developer</li><li>Web Designer</li><li>UX Engineer</li><li>Account Manager</li></ul>
  <div class="abs bottom">© Copyright 2014 <b>Company Website</b> | All Rights Reserved | Terms &amp; Conditions</div>
</footer>

</body>
</html>
```